Single-sided business card for restaurant bellwether with new logo made on this site

Business card options with new logo including restaurant name, address, phone number and website. This business card is single-sided only and will be presented at the hostess desk for clients to take. I would like to see options based on a cream card background, a white card background, a yellow card background and a burgundy colored background. It needs to be elegant and traditional.

Target Market(s)

local and international crowd

Industry/Entity Type

restaurant

Contact Information for Business Card

address, website and phone number

Font styles to use
Serif

Colors
EE7325
F08F49
F5BC92
FAE3D3
FDF4ED

Requirements
Must have
• new logo, address, phone number, website
Should not have
• more than three colors

```html
<!DOCTYPE html>
<html lang="es">
<head>
<meta charset="utf-8">
<title>Bellwether — business cards</title>
<link rel="stylesheet" href="https://fonts.googleapis.com/css2?family=Poppins:wght@500;600&display=swap">
<style>
  :root {
    --backdrop: #dcdcdc;
    --card: #f7f6f3;
    --gold: #e8b52a;
    --brand-square: #ebb033;
    --ink: #4a1e1e;
  }
  * { margin: 0; padding: 0; box-sizing: border-box; }
  html, body { width: 1200px; height: 960px; overflow: hidden; }
  body {
    position: relative;
    background: var(--backdrop);
    font-family: "Poppins", sans-serif;
    color: var(--ink);
  }
  .card {
    position: absolute;
    background: var(--card);
  }
  .card::before {
    content: "";
    position: absolute;
    inset: 9px;
    border: 5px solid var(--gold);
  }
  .card--vertical   { left: 30px;  top: 116px; width: 402px; height: 702px; }
  .card--wide-top   { left: 460px; top: 58px;  width: 703px; height: 400px; }
  .card--wide-bottom{ left: 460px; top: 480px; width: 703px; height: 400px; }

  .brand-square {
    position: absolute;
    left: 50%;
    transform: translateX(-50%);
    background: var(--brand-square);
  }
  .brand-name {
    position: absolute;
    left: 0; right: 0;
    text-align: center;
    font-weight: 600;
    text-transform: uppercase;
    line-height: 1;
  }
  .contact {
    position: absolute;
    left: 0; right: 0;
    text-align: center;
    font-weight: 600;
  }
  .contact p { white-space: nowrap; }
  .contact .gap { margin-top: 10px; }
  .dot {
    display: inline-block;
    width: 6px; height: 6px;
    border-radius: 50%;
    background: var(--gold);
    margin: 0 12px;
    vertical-align: middle;
  }

  /* vertical card */
  .card--vertical .brand-square { top: 59px; width: 150px; height: 150px; }
  .card--vertical .brand-name { top: 252px; font-size: 36px; letter-spacing: 4px; }
  .card--vertical .contact { top: 460px; font-size: 18.5px; line-height: 23px; letter-spacing: 0.4px; }
  .card--vertical .contact .gap { margin-top: 11px; }
  .card--vertical .contact .small { font-size: 16.5px; }

  /* wide cards */
  .card--wide-top .brand-square,
  .card--wide-bottom .brand-square { top: 30px; width: 114px; height: 114px; }
  .card--wide-top .brand-name,
  .card--wide-bottom .brand-name { top: 176px; font-size: 32px; letter-spacing: 4px; }

  .card--wide-top .contact { top: 276px; font-size: 17.5px; line-height: 22px; letter-spacing: 0.4px; }
  .card--wide-top .contact .gap { margin-top: 7px; font-size: 16.5px; }

  .card--wide-bottom .contact { top: 267px; font-size: 17.5px; line-height: 20px; letter-spacing: 0.4px; }
  .card--wide-bottom .contact .gap { margin-top: 9px; }
  .card--wide-bottom .contact .small { font-size: 16.5px; }
</style>
</head>
<body>

  <section class="card card--vertical" aria-label="Vertical business card">
    <div class="brand-square" aria-hidden="true"></div>
    <h1 class="brand-name">Bellwether</h1>
    <address class="contact">
      <p>Jacaranda 417</p>
      <p>Colonia Las Palmas</p>
      <p>Oaxaca, Mexico CP 70982</p>
      <p class="gap small">958-555-0142</p>
      <p class="small">www.bellwether.com.mx</p>
    </address>
  </section>

  <section class="card card--wide-top" aria-label="Horizontal business card, single contact line">
    <div class="brand-square" aria-hidden="true"></div>
    <h2 class="brand-name">Bellwether</h2>
    <address class="contact">
      <p>Jacaranda 417</p>
      <p>Colonia Las Palmas</p>
      <p>Oaxaca, Mexico CP 70982</p>
      <p class="gap">www.bellwether.com.mx<span class="dot" aria-hidden="true"></span>958-555-0142</p>
    </address>
  </section>

  <section class="card card--wide-bottom" aria-label="Horizontal business card, stacked contact">
    <div class="brand-square" aria-hidden="true"></div>
    <h2 class="brand-name">Bellwether</h2>
    <address class="contact">
      <p>Jacaranda 417</p>
      <p>Colonia Las Palmas</p>
      <p>Oaxaca, Mexico CP 70982</p>
      <p class="gap small">958-555-0142</p>
      <p class="small">www.bellwether.com.mx</p>
    </address>
  </section>

</body>
</html>
```